Cover for a Novel - German author, only e-book cover

I am a German writer and need a cover for a collection of three novels, which are already published. Please notice: I only need an e-book cover, so we do not need a blurb. The German title is "drift sideways", which can not be translated into English. Subtitle 2: Breakthrough (meaning Breakthrough) Subtitle 3: Meaning breakout (meaning breakout) (meaning "start, departure, beginning"). Subtitle 2: Breakthrough (meaning breakout) Author: Marlen Odrowska The word "crash" stems from the mechanic which is used for some elevators - where a counterweight is needed to leap up the cabin.) The protagonist Corinna has brown hair, she is not blond. You can work with symbols. (But please do not be boring about the career) See the covers of my books, but please feel free to have your own ideas. The story in short: A 23-year-old girl, Corinna, is a complete orphan , laquer of money and self-consciousness. She is shy and not open to the world. In fact she is afraid of the world. Her stepfather is an alcoholic, her stepmother overworked and overchallenged. Corinna studies at university, struggles for a better life, but feels in every respect underprivileged. In this time (the Nineties) companies with multi-level marketing systems spring up like mushrooms. Naively she slides into one of them - which is a very bad reputation in Germany. A path of trial and tribulation and she decides - against all odds - go go the rocky road. But she clums her teeth, holds her ground in a male world, where her way up to the top. She falls in love with her boss and the relationship ends in an disaster. So she focuses on her work, but with increasing maturity, she asks herself what is really important in life - she recognizes that material success is not possible, is not durable, if she dosn't find her inner strength. And then another one enters the stage ... and shows here, what life is really all about. And the second thing is that these volumes enter into the multi-level Marketing Systems of the Nineties. To the designers: if you have any questions, do not hesitate to ask me.

Target Market(s)

Readers from 18 plus, men and women, who wants to have a better life

Font styles to use
Serif

Requirements
Must have
• eye-catching, classy, ​​elegant, timeless
Nice to have
• Feelings which should be expressed: The hunger and longing for a good life without money-problems. The strength to hold on, the desire for happiness, the long-term to live an independent and fulfilled life.
Should not have
• no sex scenes on the cover please

```html
<!DOCTYPE html>
<html lang="de">
<head>
<meta charset="utf-8">
<title>Drift Sideways – Wendung</title>
<link href="https://fonts.googleapis.com/css2?family=Cinzel:wght@400;500&family=Great+Vibes&display=swap" rel="stylesheet">
<style>
  :root {
    --night: #050505;
    --ink: #141213;
    --paper: #ffffff;
    --skin-light: #d4c2c2;
    --skin-mid: #a8959a;
    --skin-shade: #6d5f66;
    --hair: #2b2320;
  }
  html, body {
    margin: 0;
    padding: 0;
    width: 800px;
    height: 1200px;
    overflow: hidden;
    background: var(--night);
  }
  .cover {
    position: relative;
    width: 800px;
    height: 1200px;
    overflow: hidden;
    background: var(--night);
  }
  .cover-photo {
    position: absolute;
    inset: 0;
    background:
      radial-gradient(ellipse 200px 190px at 410px 560px, var(--hair) 0%, rgba(43,35,32,0.6) 60%, rgba(5,5,5,0) 100%),
      radial-gradient(ellipse 470px 460px at 410px 1160px, var(--skin-light) 0%, var(--skin-mid) 45%, var(--skin-shade) 72%, rgba(5,5,5,0) 100%),
      var(--night);
  }
  .author {
    position: absolute;
    top: 8px;
    left: 0;
    right: 0;
    margin: 0;
    text-align: center;
    font-family: "Cinzel", serif;
    font-weight: 400;
    font-size: 48px;
    line-height: 1.3;
    letter-spacing: 0.36em;
    margin-right: -0.36em;
    color: var(--paper);
  }
  .volume-title {
    position: absolute;
    top: 150px;
    left: 0;
    right: 0;
    margin: 0;
    text-align: center;
    font-family: "Great Vibes", cursive;
    font-weight: 400;
    font-size: 170px;
    line-height: 1.2;
    color: var(--paper);
  }
  .series {
    position: absolute;
    top: 958px;
    left: 0;
    right: 0;
    margin: 0;
    text-align: center;
    font-family: "Cinzel", serif;
    font-weight: 400;
    color: var(--ink);
  }
  .series-main {
    display: block;
    font-size: 92px;
    line-height: 1;
    letter-spacing: 0.5em;
    margin-right: -0.5em;
  }
  .series-sub {
    display: block;
    margin-top: 8px;
    font-size: 58px;
    line-height: 1;
    letter-spacing: 0.42em;
    margin-right: -0.42em;
  }
  .edition {
    display: block;
    margin-top: 12px;
    font-size: 30px;
    line-height: 1;
    letter-spacing: 0.3em;
    margin-right: -0.3em;
  }
</style>
</head>
<body>
  <main class="cover">
    <div class="cover-photo" role="img" aria-label="Photograph of a brown-haired young woman seen from behind with bare shoulders, holding white chrysanthemums against her shoulder, on a black background"></div>
    <p class="author">Marlen Odrowska</p>
    <h2 class="volume-title">Wendung</h2>
    <h1 class="series">
      <span class="series-main">DRIFT</span>
      <span class="series-sub">SIDEWAYS</span>
      <span class="edition">GESAMTAUSGABE</span>
    </h1>
  </main>
</body>
</html>
```